Criação de Logotipo + Papelaria Profissional + Manual para Contabilidade & Finanças
" Possui planos de investimentos e o cliente realiza a contratação e recebe rendimentos diários "

```html
<!DOCTYPE html>
<html lang="pt-BR">
<head>
<meta charset="UTF-8">
<title>Veltra Investimentos – Capa</title>
<link rel="stylesheet" href="https://fonts.googleapis.com/css2?family=Titillium+Web:wght@300;700&display=swap">
<style>
  :root {
    --page: #ffffff;
    --band-light: #3f8fc6;
    --band-mid: #2a74ad;
    --band-dark: #1a5a8e;
    --brand-green: #7fd3a8;
    --white: #ffffff;
    --photo-top: #6f9fd0;
    --photo-bottom: #2f6ea5;
  }
  * { margin: 0; padding: 0; box-sizing: border-box; }
  html, body {
    width: 1200px;
    height: 1200px;
    overflow: hidden;
    background: var(--page);
    font-family: "Titillium Web", sans-serif;
  }
  .canvas {
    position: relative;
    width: 1200px;
    height: 1200px;
    background: var(--page);
  }
  .cover-band {
    position: absolute;
    left: 0;
    top: 384px;
    width: 1200px;
    height: 437px;
    background:
      radial-gradient(ellipse 700px 420px at 620px 200px, var(--band-light) 0%, var(--band-mid) 55%, var(--band-dark) 100%);
    overflow: hidden;
  }
  .portrait-area {
    position: absolute;
    left: 36px;
    top: 0;
    width: 348px;
    height: 437px;
    background: linear-gradient(180deg, var(--photo-top) 0%, var(--photo-bottom) 100%);
    border-radius: 160px 160px 0 0;
    opacity: 0.85;
  }
  .brand-lockup {
    position: absolute;
    left: 510px;
    top: 78px;
    width: 420px;
    text-align: center;
  }
  .brand-name {
    font-weight: 300;
    font-size: 190px;
    line-height: 1;
    letter-spacing: 2px;
    color: var(--brand-green);
  }
  .tagline {
    display: inline-block;
    margin-top: 0;
    padding: 2px 16px;
    border: 3px solid var(--white);
    border-radius: 4px;
    font-weight: 700;
    font-size: 30px;
    letter-spacing: 0.5px;
    color: var(--white);
    line-height: 1.3;
  }
  .web-address {
    position: absolute;
    right: 26px;
    top: 354px;
    font-weight: 300;
    font-size: 22px;
    color: var(--white);
  }
  .social-row {
    position: absolute;
    right: 54px;
    top: 394px;
    display: flex;
    gap: 12px;
  }
  .social-dot {
    width: 30px;
    height: 30px;
    border-radius: 50%;
    background: var(--white);
  }
</style>
</head>
<body>
  <main class="canvas">
    <section class="cover-band">
      <div class="portrait-area" role="img" aria-label="Foto de um homem de camisa azul com os braços cruzados"></div>

      <div class="brand-lockup">
        <div class="brand-name">Veltra</div>
        <div class="tagline">BEM-VINDO AO SEU SUCESSO</div>
      </div>

      <p class="web-address">www.veltrainvestimentos.com.br</p>

      <div class="social-row" aria-label="Redes sociais">
        <span class="social-dot"></span>
        <span class="social-dot"></span>
        <span class="social-dot"></span>
        <span class="social-dot"></span>
        <span class="social-dot"></span>
      </div>
    </section>
  </main>
</body>
</html>
```